Super Fast Need - Complet Project In 48 Hours - Simple MS Word Layout

Okay my designer is having some family emergencies so I stuck with an super quick need. Basically, I need two hand outs put together. We are having a 4 day seminar with 2 separate events. Each event has sessions where the speaker for that session will make presentation and the audience will have a page to reference with fill in the blanks to follow along with the speaker during the presentation. The first event has 24 sessions so there will be a hand out with 24 reference pages handed to the audience for this event and the other event about 30 so there will be handout with 30 pages.

I have included a sample of what we have done in the past so you can reference exactly what I am talking about.

So the assignment would be:

1.) Take each of fill in the blank notes page for each session. (provided in msword)
2.) Clean it up.
3.) Put them in order into one MS word Document. (You can even use the format of what we have if you want.)
4.) Thats it other than make it look professional.

Now here is the challenge I can give you all the files to you today, but I need it totally completed by Sunday noon NY time USA, October 13th. That is less than 3 days.

Attachments -

An example of the finished hand out needed for each of the two events.

An example of the individual notes that need to be cleaned up and put in the proper order of the handout.

A agenda so you can see how the two events are ordered.

my sypke is kal.morvick if you have questions.

Industry/Entity Type

Events

```html
<!DOCTYPE html>
<html lang="en">
<head>
<meta charset="utf-8">
<title>Session 5 – Time Management / Real Business</title>
<link href="https://fonts.googleapis.com/css2?family=Carlito:wght@400;700&display=swap" rel="stylesheet">
<style>
  :root {
    --page: #ffffff;
    --ink: #1c1c1c;
    --heading: #3b3b3b;
    --muted: #5a5a5a;
    --speaker: #6a6a6a;
    --rule: #6f6f6f;
  }
  * { margin: 0; padding: 0; box-sizing: border-box; }
  html, body { width: 927px; height: 1200px; overflow: hidden; background: var(--page); }
  body { font-family: "Carlito", "Calibri", Arial, sans-serif; color: var(--ink); position: relative; }

  .session-title { position: absolute; left: 131px; top: 88px; font-size: 21px; font-weight: 700; letter-spacing: -0.2px; }
  .speaker { position: absolute; left: 139px; top: 128px; font-size: 18px; color: var(--speaker); }

  .topic { position: absolute; left: 131px; width: 700px; }
  .topic h2 { font-size: 18.5px; font-weight: 700; color: var(--heading); line-height: 22px; }

  .points { list-style: none; font-size: 14.5px; line-height: 20.4px; margin-top: 15px; }
  .points > li { position: relative; padding-left: 53px; }
  .points > li::before { content: ""; position: absolute; left: 28px; top: 8px; width: 5px; height: 5px; border-radius: 50%; background: var(--ink); }

  .points--soft { color: var(--muted); line-height: 27px; margin-top: 17px; }
  .points--soft > li { padding-left: 79px; }
  .points--soft > li::before { left: 56px; top: 11px; background: var(--ink); }

  .ticks { list-style: none; }
  .ticks li { position: relative; padding-left: 53px; height: 20.2px; }
  .ticks li::before { content: "✓"; position: absolute; left: 27px; top: -1px; font-size: 15px; color: var(--ink); }

  .blank { display: inline-block; width: var(--w, 80px); height: 1px; border-bottom: 1px dotted var(--rule); vertical-align: 3px; margin: 0 3px; }
  .blank--tight { margin: 0 1px; }
</style>
</head>
<body>
  <h1 class="session-title">SESSION5–Time Management/Real Business</h1>
  <p class="speaker">Dale Whitcomb</p>

  <section class="topic" style="top:210px">
    <h2>You Own A Real Business</h2>
    <ul class="points points--soft">
      <li>One of the many benefits is the <span class="blank" style="--w:128px"></span> of entry.</li>
      <li>This can also be a <span class="blank" style="--w:124px"></span> too.</li>
      <li>Because many people do <span class="blank" style="--w:124px"></span> it as the<span class="blank blank--tight" style="--w:118px"></span> business it is.</li>
    </ul>
  </section>

  <section class="topic" style="top:360px">
    <h2>You Have A Million Dollar Image …</h2>
    <ul class="points">
      <li>Without investing <span class="blank" style="--w:82px"></span> of <span class="blank" style="--w:122px"></span> of your personal money.</li>
      <li>Ned Farrow and Gil Parsons are <span class="blank" style="--w:82px"></span> and <span class="blank" style="--w:84px"></span> business leaders.</li>
      <li>You have 100’s of employees who provide:
        <ul class="ticks">
          <li><span class="blank" style="--w:110px"></span></li>
          <li><span class="blank" style="--w:110px"></span></li>
          <li><span class="blank" style="--w:110px"></span></li>
          <li><span class="blank" style="--w:110px"></span></li>
          <li><span class="blank" style="--w:110px"></span></li>
          <li><span class="blank" style="--w:110px"></span></li>
        </ul>
      </li>
    </ul>
  </section>

  <section class="topic" style="top:619px">
    <h2>Real Businesses Have Business Hours</h2>
    <ul class="points">
      <li>Treat it like a <span class="blank" style="--w:72px"></span> – get <span class="blank" style="--w:72px"></span> results</li>
      <li>Treat it like a <span class="blank" style="--w:72px"></span> – get <span class="blank" style="--w:72px"></span> results</li>
      <li>You must have <span class="blank" style="--w:72px"></span> and <span class="blank" style="--w:74px"></span> your business</li>
    </ul>
  </section>

  <section class="topic" style="top:759px">
    <h2>How ToBuild A Business Without Sacrificing Your Entire Life</h2>
    <ul class="points">
      <li>Everyone has the <span class="blank" style="--w:108px"></span> of hours.</li>
      <li><span class="blank blank--tight" style="--w:110px"></span></li>
      <li>You have all the<span class="blank blank--tight" style="--w:70px"></span>you <span class="blank" style="--w:72px"></span> to build a successful business.</li>
    </ul>
  </section>

  <section class="topic" style="top:900px">
    <h2>Finding TimeTo Build A Successful Business</h2>
    <ul class="points">
      <li>7 hours to sponsor one person into the business
        <ul class="ticks"><li><span class="blank" style="--w:36px"></span> hours per month to sponsor <span class="blank" style="--w:36px"></span></li></ul>
      </li>
      <li>2 hours per placement to share the technology
        <ul class="ticks"><li><span class="blank blank--tight" style="--w:36px"></span>hours per month to place <span class="blank" style="--w:36px"></span> units per week</li></ul>
      </li>
      <li>1 hour per support call
        <ul class="ticks"><li><span class="blank" style="--w:36px"></span> hours per month to stay plugged into <span class="blank" style="--w:72px"></span></li></ul>
      </li>
      <li><span class="blank" style="--w:36px"></span> total hours per month or <span class="blank" style="--w:36px"></span> hours per week!</li>
    </ul>
  </section>
</body>
</html>
```